LUMINARA VENTURES NAMECARD

Need to design a name card with an existing logo.

As we are professional corporate services provider our name card has to project a professional image.
Should be corporate, simple & professional.

Our corporate color is maroon red but not too dull.

Please refer to our website at www.luminaraventures.com.sg

Would attach our logo herewith.

Front surface of namecard details:
LUMINARA VENTURES PTE LTD
Registration No. 208711845K

Tan Wei Ling CA (Singapore)
Director

Tel +65 6481 2957
Mobile +65 9172 3086
tan@luminaraventures.com.sg
www.luminaraventures.com.sg

47 Plover Lane
#07-12 Harbourlight Plaza
Singapore 276351

Back of namecard:-
OUR CORE SERVICES
Incorporation services
Corporate Secretarial Services
Accountancy service
Goods & Services Taxation
Corporate & Personal Taxation
Financial Reporting
Payroll Administration

AFFILIATES:
BRIGHTWAVE CORPORATE SERVICES PTE LTD
PINNACLEFORMATIONSPTE LTD
LIM MANAGEMENT SERVICES PTE LTD
RW HO AND COMPANY PTE LTD
LEDGERLY ACADEMY

```html
<!DOCTYPE html>
<html lang="en">
<head>
<meta charset="utf-8">
<title>Luminara Ventures Namecard</title>
<link rel="stylesheet" href="https://fonts.googleapis.com/css2?family=Oswald:wght@500;600&family=Work+Sans:wght@400;500;600&family=Roboto+Condensed:wght@400;500&display=swap">
<style>
  :root{
    --brand-red:#cf1f2e;
    --ink:#2b2b2b;
    --muted:#6b6b6b;
    --card:#ffffff;
    --backdrop:#8e8d8e;
  }
  *{margin:0;padding:0;box-sizing:border-box}
  html,body{width:1200px;height:900px;overflow:hidden}
  body{background:var(--backdrop);position:relative;font-family:"Work Sans",sans-serif;color:var(--ink)}
  .card{position:absolute;width:560px;height:320px;background:var(--card);box-shadow:0 6px 18px rgba(0,0,0,.28);overflow:hidden}
  .card--front{left:50px;top:80px}
  .card--back{left:590px;top:500px}

  .edge-bar{position:absolute;left:0;width:9px;background:var(--brand-red)}

  .logo{position:absolute;font-family:"Work Sans",sans-serif;font-weight:600;color:var(--brand-red);line-height:.95;letter-spacing:.5px;text-transform:uppercase}

  /* front */
  .card--front .logo{left:300px;top:38px;font-size:26px}
  .reg{position:absolute;left:40px;top:82px;font-size:10px;color:var(--ink)}
  .reg span{color:var(--brand-red)}
  .person{position:absolute;left:40px;top:190px}
  .person__name{font-family:"Oswald",sans-serif;font-weight:600;font-size:26px;color:var(--brand-red);letter-spacing:.3px;line-height:1}
  .person__role{font-size:15px;color:var(--muted);font-weight:500;letter-spacing:.5px;margin-top:3px}
  .card--front .edge-bar{top:192px;height:52px}
  .address{position:absolute;left:300px;top:120px;font-size:12px;line-height:1.3;letter-spacing:.4px}
  .contacts{position:absolute;left:300px;top:196px;list-style:none;font-size:12px;line-height:1.35;letter-spacing:.3px}
  .contacts li{display:flex;align-items:center;gap:10px}
  .contacts svg{width:11px;height:11px;flex:none;fill:none;stroke:var(--brand-red);stroke-width:1.6}

  /* back */
  .services{position:absolute;left:300px;top:34px}
  .services__title{font-size:13px;font-weight:500;color:var(--brand-red);letter-spacing:.5px;margin-bottom:4px}
  .services__list{list-style:none;font-size:12.5px;line-height:1.42;letter-spacing:.2px}
  .services__list li{display:flex;align-items:center;gap:9px}
  .services__list li::before{content:"";width:6px;height:6px;background:var(--brand-red);transform:rotate(45deg);flex:none;margin-left:4px}
  .card--back .logo{left:40px;top:150px;font-size:30px}
  .card--back .edge-bar{top:150px;height:58px}
  .affiliates__label{position:absolute;left:40px;top:236px;font-size:13px;font-weight:500;color:var(--brand-red);letter-spacing:.6px}
  .affiliates__band{position:absolute;left:0;right:0;bottom:0;height:62px;background:var(--brand-red);color:#fff;font-family:"Roboto Condensed",sans-serif;font-size:10.5px;letter-spacing:.2px;padding:14px 40px 0;line-height:1.55;text-transform:uppercase}
</style>
</head>
<body>

<section class="card card--front" aria-label="Namecard front">
  <div class="logo">Luminara<br>Ventures</div>
  <p class="reg"><span>Reg. No:</span> 208711845K</p>
  <div class="edge-bar"></div>
  <div class="person">
    <p class="person__name">TAN WEI LING CA</p>
    <p class="person__role">DIRECTOR</p>
  </div>
  <address class="address" style="font-style:normal">
    47 Plover Lane<br>#07-12 Harbourlight Plaza<br>Singapore 276351
  </address>
  <ul class="contacts">
    <li><svg viewBox="0 0 12 12"><path d="M2 1.5l2 0 1 2.5-1.3 1a6 6 0 0 0 3.3 3.3l1-1.3 2.5 1v2a1 1 0 0 1-1 1A9 9 0 0 1 1 2.5a1 1 0 0 1 1-1z"/></svg>+65 6481 2957</li>
    <li><svg viewBox="0 0 12 12"><rect x="3" y="1" width="6" height="10" rx="1"/><path d="M5.3 9.2h1.4"/></svg>+65 9172 3086</li>
    <li><svg viewBox="0 0 12 12"><rect x="1" y="2.5" width="10" height="7"/><path d="M1 2.5l5 4 5-4"/></svg>tan@luminaraventures.com.sg</li>
    <li><svg viewBox="0 0 12 12"><circle cx="5" cy="5" r="3.5"/><path d="M7.6 7.6L11 11"/></svg>www.luminaraventures.com.sg</li>
  </ul>
</section>

<section class="card card--back" aria-label="Namecard back">
  <div class="services">
    <p class="services__title">OUR CORE SERVICES</p>
    <ul class="services__list">
      <li>Incorporation services</li>
      <li>Corporate Secretarial Services</li>
      <li>Accountancy service</li>
      <li>Goods &amp; Services Taxation</li>
      <li>Corporate &amp; Personal Taxation</li>
      <li>Financial Reporting</li>
      <li>Payroll Administration</li>
    </ul>
  </div>
  <div class="edge-bar"></div>
  <div class="logo">Luminara<br>Ventures</div>
  <p class="affiliates__label">AFFILIATES</p>
  <div class="affiliates__band">
    Brightwave Corporate Services Pte Ltd | PinnacleFormationsPte Ltd<br>
    Lim Management Services Pte Ltd | RW Ho and Company Pte Ltd | Ledgerly Academy
  </div>
</section>

</body>
</html>
```